Business Card Design

We require a business card design for a law firm, our signature colours are maroon and cream. Our slogan is "From our family to yours", we would like the cards to be professional however feminine at the same time.

Industry/Entity Type

Business

Contact Information for Business Card

Helena Brackett & Associates Lawyers & Conveyancers, Helena Brackett LL.B. Principal Solicitor, 17 Quillon Street, Marrowdale NSW 2190

Logo styles of interest
Emblem Logo
Abstract Logo
Wordmark Logo

```html
<!DOCTYPE html>
<html lang="en">
<head>
<meta charset="utf-8">
<title>Helena Brackett &amp; Associates – Business Card</title>
<link rel="stylesheet" href="https://fonts.googleapis.com/css2?family=Crimson+Text:wght@400;600&family=Pinyon+Script&display=swap">
<style>
  :root {
    --cream: #fff6cc;
    --maroon: #a8403f;
    --ink: #1a1a1a;
    --border: #222;
    --serif: "Crimson Text", "Times New Roman", serif;
    --script: "Pinyon Script", cursive;
  }
  html, body {
    margin: 0;
    padding: 0;
    width: 1200px;
    height: 687px;
    overflow: hidden;
    background: #ffffff;
  }
  .card {
    position: relative;
    width: 1200px;
    height: 687px;
    box-sizing: border-box;
    background: var(--cream);
    border: 2px solid var(--border);
    border-top-left-radius: 215px;
    overflow: hidden;
    font-family: var(--serif);
    color: var(--ink);
  }
  .corner-tab {
    position: absolute;
    top: 0;
    right: 0;
    width: 50px;
    height: 331px;
    background: var(--maroon);
    border-bottom-left-radius: 18px;
  }
  .emblem {
    position: absolute;
    left: 516px;
    top: 40px;
    width: 170px;
    height: 178px;
    border-radius: 50% 50% 40% 40%;
    background: radial-gradient(circle at 50% 45%, #3a3430 0%, #8a7f6a 55%, rgba(255,246,204,0) 75%);
  }
  .firm-name {
    position: absolute;
    left: 0;
    width: 1200px;
    top: 227px;
    margin: 0;
    text-align: center;
    font-size: 48px;
    font-weight: 600;
    line-height: 1;
    color: var(--maroon);
  }
  .firm-type {
    position: absolute;
    left: 0;
    width: 1200px;
    top: 287px;
    margin: 0;
    text-align: center;
    font-size: 35px;
    line-height: 1;
  }
  .rule {
    position: absolute;
    left: 536px;
    top: 354px;
    width: 122px;
    height: 2px;
    background: var(--maroon);
  }
  .slogan {
    position: absolute;
    left: 0;
    width: 1200px;
    top: 395px;
    margin: 0;
    text-align: center;
    font-family: var(--script);
    font-size: 56px;
    line-height: 1;
  }
  .address {
    position: absolute;
    right: 830px;
    top: 540px;
    margin: 0;
    text-align: right;
    font-style: normal;
    font-size: 31px;
    line-height: 47px;
  }
  .divider {
    position: absolute;
    left: 422px;
    top: 533px;
    width: 14px;
    height: 160px;
    background: var(--maroon);
  }
  .contact {
    position: absolute;
    left: 487px;
    top: 526px;
  }
  .contact-name {
    margin: 0;
    font-size: 44px;
    line-height: 1;
    color: var(--maroon);
  }
  .contact-role {
    margin: 14px 0 0;
    font-size: 31px;
    line-height: 1;
  }
</style>
</head>
<body>
  <main class="card">
    <div class="corner-tab"></div>
    <div class="emblem" role="img" aria-label="Firm emblem: scales of justice with decorative scrollwork"></div>
    <h1 class="firm-name">Helena Brackett &amp; Associates</h1>
    <p class="firm-type">Lawyers &amp; Conveyancers</p>
    <div class="rule"></div>
    <p class="slogan">From our family to yours</p>
    <address class="address">17 Quillon Street<br>Marrowdale NSW 2190</address>
    <div class="divider"></div>
    <div class="contact">
      <p class="contact-name">Helena Brackett LL.B</p>
      <p class="contact-role">Principal Solicitor</p>
    </div>
  </main>
</body>
</html>
```